Dr. Lumora needs a design for its website!

*Only need the design, coding is not required.
*Need desktop version ($500) and mobile/tablet version ($200)
*The attached files are not the exact layout we want, they are just for you to know what information should be included in those pages.
*The function of our website is like www.qtv-medlist.example
*For the background picture, prefer a lively picture and chinese people in it, NOT necessarily need a doctor or sick person in the picture

***Don't just copy the layout from the attachments or from the reference website, we are looking for creative ideas, non-ordinary designs!!!****

We are developing a website for the public to search a doctor by different criteria. At the initial stage, we need 4 pages to start with and other pages at later stage. I have attached the general idea of these pages but not necessarily to be exactly the same, I am looking for some new ideas.

This website needs a professional, modern, simple and user friendly design. The main color to be used in the website will be same as the color (R:0 G:139 B:205) used in our logo (see attached). We don't have any particular thoughts for the other color and the font to be used in the website. Can try to use circle outline for the icon in the navigation bar.

1. Home: will include 4 sections (see attached)

2. Doctor's details (see attached)

3. Health information: will include a short descriptions of this Health Info page and 5 sections (see attached)

4. News (see attached)

Reason: Not too many suitable designs to choose from and need more time to go through the designs

Target Market(s)

All

Industry/Entity Type

Medical

Number of Pages Required

4 page

Requirements
Should not have
• must not be same as or looks too much like www.qtv-medlist.example
• prefer not to use black and red color

```html
<!DOCTYPE html>
<html lang="en">
<head>
<meta charset="utf-8">
<title>Dr. Lumora – Home</title>
<link rel="stylesheet" href="https://fonts.googleapis.com/css2?family=Montserrat:wght@400;500&family=Open+Sans:wght@400;600&display=swap">
<style>
:root{
  --brand:#008bcd;
  --brand-dark:#0a78b5;
  --brand-soft:#5aa6d6;
  --topbar:#3a3a3a;
  --ink:#444;
  --muted:#999;
  --line:#c9c9c9;
  --band:#efefef;
  --white:#fff;
}
*{box-sizing:border-box;margin:0;padding:0}
html,body{width:751px;height:1200px;overflow:hidden;background:var(--white)}
body{position:relative;font-family:"Open Sans",sans-serif;color:var(--ink)}
.abs{position:absolute}

/* hero */
.hero{left:0;top:0;width:751px;height:474px;
  background:radial-gradient(ellipse at 60% 55%,#e9d8c4 0%,#d9d2c8 35%,#cfd3cf 65%,#e6e6e2 100%)}
.topbar{left:0;top:0;width:751px;height:13px;background:var(--topbar);
  font-family:"Montserrat",sans-serif;font-size:5px;color:#ddd;letter-spacing:.2px}
.lang{top:3px;display:flex;align-items:center;gap:3px}
.lang i{display:block;width:7px;height:7px;border-radius:50%}
.lang-sep{left:660px;top:3px;width:1px;height:7px;background:#888}
.brand{left:44px;top:30px;display:flex;align-items:center;gap:8px}
.brand-dot{width:36px;height:36px;border-radius:50%;background:var(--brand)}
.brand-name{font-family:"Open Sans",sans-serif;font-weight:600;font-size:27px;color:var(--brand)}
.search{left:456px;top:38px;width:168px;height:21px;border-radius:11px;background:rgba(255,255,255,.92);
  border:1px solid #ddd;font-size:8px;color:#aaa;padding:5px 10px}
.search svg{position:absolute;right:8px;top:4px}
.login{left:648px;top:39px;width:55px;height:20px;background:#3a3a3a;color:#fff;
  font-family:"Montserrat",sans-serif;font-size:8.5px;display:flex;align-items:center;justify-content:center;border:1px solid #777}

/* nav */
.nav{left:0;top:474px;width:751px;height:44px;background:#fafafa;border-bottom:2px solid var(--brand);
  font-family:"Montserrat",sans-serif;font-size:11px;color:var(--brand)}
.nav-item{position:absolute;top:0;height:42px;line-height:42px;transform:translateX(-50%)}
.nav-home{position:absolute;left:107px;top:0;width:55px;height:42px;background:var(--brand);color:#fff;text-align:center;line-height:42px}

/* member */
.member{left:0;top:518px;width:751px;height:300px;
  background:linear-gradient(120deg,#9cccec 0%,#7fbbe3 30%,#64a9d8 55%,#8cc3e6 80%,#a9d3ef 100%)}
.member-title{left:47px;top:556px;font-size:20.5px;color:#fff}
.perk{left:76px;display:flex;align-items:center;gap:10px;font-family:"Montserrat",sans-serif;font-size:13.5px;color:#fff}
.signup-card{left:374px;top:534px;width:348px;height:271px;border-radius:10px;background:rgba(220,238,250,.75)}
.field{position:absolute;height:26px;background:#fff;border:1px solid var(--brand-soft);
  font-family:"Montserrat",sans-serif;font-size:10.5px;color:var(--brand-soft);padding:5px 9px}
.dob-label{left:387px;top:721px;font-family:"Montserrat",sans-serif;font-size:12px;color:var(--brand)}
.select{position:absolute;top:716px;height:26px;background:#fff;border:1px solid var(--brand-soft);
  font-family:"Montserrat",sans-serif;font-size:10.5px;color:var(--brand-soft);display:flex}
.select span{flex:1;text-align:center;line-height:24px}
.select b{width:23px;border-left:1px solid var(--brand-soft);display:flex;align-items:center;justify-content:center}
.btn-signup{left:512px;top:766px;width:65px;height:23px;background:var(--brand);color:#fff;
  font-family:"Montserrat",sans-serif;font-size:10px;display:flex;align-items:center;justify-content:center;border:1px solid #0b6fa6}

/* finder */
.finder{left:0;top:818px;width:751px;height:101px;background:var(--band)}
.finder-tab{left:0;top:818px}
.finder-title{left:53px;top:856px;font-size:20.5px;color:#fff}
.label{position:absolute;font-size:7.5px;color:#555}
.input{position:absolute;height:14px;background:#fff;border:1px solid var(--line);border-radius:2px}
.dd{position:absolute;height:12px;background:#fff;border:1px solid var(--line);font-size:5.5px;color:#aaa;padding:2px 4px}
.dd::after{content:"";position:absolute;right:3px;top:4px;border:2.5px solid transparent;border-top:3px solid #555}
.radio{position:absolute;width:8px;height:8px;border-radius:50%;border:1px solid #999;background:#fff}
.radio.on::after{content:"";position:absolute;left:1.5px;top:1.5px;width:3px;height:3px;border-radius:50%;background:#333}
.btn{position:absolute;top:890px;height:17px;font-size:8px;display:flex;align-items:center;justify-content:center}
.btn-reset{left:578px;width:52px;background:#fff;border:1px solid var(--brand);color:var(--brand)}
.btn-search{left:650px;width:53px;background:var(--brand);color:#fff}

/* results */
.results{left:25px;top:936px;width:700px;height:238px;border:1px solid #ddd;border-radius:13px;background:#fff}
.empty{left:0;width:751px;top:1046px;display:flex;justify-content:center;align-items:center;gap:6px;font-size:10px;color:var(--brand)}
.footer{left:0;width:751px;top:1183px;text-align:center;font-size:6px;color:#888}
</style>
</head>
<body>

<div class="abs hero" role="img" aria-label="Photo of a smiling father and two young daughters looking at a tablet together on a sofa in a bright living room"></div>

<div class="abs topbar">
  <div class="abs lang" style="left:621px"><i style="background:#7a8fc4"></i>ENGLISH</div>
  <div class="abs lang-sep"></div>
  <div class="abs lang" style="left:666px"><i style="background:#d64545"></i>CHINESE</div>
</div>

<div class="abs brand"><div class="brand-dot"></div><div class="brand-name">Dr. Lumora</div></div>

<div class="abs search">Search . . .
  <svg width="12" height="12" viewBox="0 0 12 12"><circle cx="5" cy="5" r="4" fill="none" stroke="#5aa6d6" stroke-width="1.2"/><line x1="8" y1="8" x2="11" y2="11" stroke="#5aa6d6" stroke-width="1.2"/></svg>
</div>
<div class="abs login">LOG IN</div>

<nav class="abs nav">
  <div class="nav-home">Home</div>
  <div class="nav-item" style="left:219px">Doctor List</div>
  <div class="nav-item" style="left:336px">Health Information</div>
  <div class="nav-item" style="left:438px">News</div>
  <div class="nav-item" style="left:518px">About Us</div>
  <div class="nav-item" style="left:612px">Contact Us</div>
</nav>

<section class="abs member"></section>
<h2 class="abs member-title" style="font-weight:400">Become a Dr. Lumora Member</h2>
<div class="abs perk" style="top:604px"><svg width="18" height="16" viewBox="0 0 18 16"><path d="M2 9 L6 14 L16 1" fill="none" stroke="#fff" stroke-width="2"/></svg>First- hand health news</div>
<div class="abs perk" style="top:641px"><svg width="18" height="16" viewBox="0 0 18 16"><path d="M2 9 L6 14 L16 1" fill="none" stroke="#fff" stroke-width="2"/></svg>Exclusive promotions</div>
<div class="abs perk" style="top:679px"><svg width="18" height="16" viewBox="0 0 18 16"><path d="M2 9 L6 14 L16 1" fill="none" stroke="#fff" stroke-width="2"/></svg>Instant health advices</div>
<div class="abs perk" style="top:717px"><svg width="18" height="16" viewBox="0 0 18 16"><path d="M2 9 L6 14 L16 1" fill="none" stroke="#fff" stroke-width="2"/></svg>Free health seminars or talk</div>
<div class="abs perk" style="top:754px"><svg width="18" height="16" viewBox="0 0 18 16"><path d="M2 9 L6 14 L16 1" fill="none" stroke="#fff" stroke-width="2"/></svg>Priority doctor appointments</div>

<div class="abs signup-card"></div>
<div class="field" style="left:386px;top:554px;width:153px">First Name</div>
<div class="field" style="left:555px;top:554px;width:154px">Last Name</div>
<div class="field" style="left:386px;top:593px;width:323px">Email address</div>
<div class="field" style="left:386px;top:634px;width:323px">New password</div>
<div class="field" style="left:386px;top:674px;width:323px">Re-enter password</div>
<div class="abs dob-label">Date of Birth</div>
<div class="select" style="left:467px;width:85px"><span>Month</span><b><svg width="9" height="6"><path d="M0 0H9L4.5 6Z" fill="#008bcd"/></svg></b></div>
<div class="select" style="left:557px;width:62px"><span>Day</span><b><svg width="9" height="6"><path d="M0 0H9L4.5 6Z" fill="#008bcd"/></svg></b></div>
<div class="select" style="left:624px;width:85px"><span>Year</span><b><svg width="9" height="6"><path d="M0 0H9L4.5 6Z" fill="#008bcd"/></svg></b></div>
<div class="abs btn-signup">SIGN UP</div>

<section class="abs finder"></section>
<svg class="abs finder-tab" width="232" height="101" viewBox="0 0 232 101"><path d="M0 0H176L230 101H0Z" fill="#0a8fd2"/>
  <circle cx="30" cy="49" r="7" fill="none" stroke="#fff" stroke-width="1.5"/><path d="M24 58 Q30 66 36 58" fill="none" stroke="#fff" stroke-width="1.5"/></svg>
<div class="abs finder-title">Find a Doctor</div>

<div class="label" style="left:223px;top:837px">Doctor's Name:</div>
<div class="input" style="left:286px;top:834px;width:232px"></div>
<div class="label" style="left:247px;top:868px">Gender:</div>
<div class="radio on" style="left:287px;top:869px"></div><div class="label" style="left:301px;top:869px;font-size:6.5px">Male</div>
<div class="radio" style="left:287px;top:887px"></div><div class="label" style="left:301px;top:887px;font-size:6.5px">Female</div>
<div class="label" style="left:362px;top:865px">Phone Number:</div>
<div class="input" style="left:427px;top:864px;width:91px;height:12px"></div>
<div class="label" style="left:362px;top:891px">Specialism:</div>
<div class="dd" style="left:427px;top:890px;width:91px">Select a specialism</div>
<div class="label" style="left:554px;top:837px">Symptoms:</div>
<div class="dd" style="left:606px;top:836px;width:106px">Select a symptom</div>
<div class="label" style="left:554px;top:865px">District:</div>
<div class="dd" style="left:606px;top:864px;width:106px">Select a district</div>
<div class="btn btn-reset">RESET</div>
<div class="btn btn-search">SEARCH</div>

<section class="abs results"></section>
<div class="abs empty"><svg width="12" height="12" viewBox="0 0 12 12"><circle cx="5" cy="5" r="4" fill="none" stroke="#008bcd" stroke-width="1.2"/><line x1="8" y1="8" x2="11" y2="11" stroke="#008bcd" stroke-width="1.2"/></svg>No Results Found</div>

<footer class="abs footer">© Dr. Lumora. All Rights Reserved.</footer>
</body>
</html>
```